【希望イメージ】
・信頼感
・成長力がある
・明るい(話しやすい、相談しやすい)

【ロゴのイメージ】
左側はハルミナスの「F」をモチーフに、右側はお客様をイメージし、手と手を取り合って成長していく(右肩上がり)イメージです。オレンジを入れることで明るさや親しみやすさを出しています。あとは青い炎のような感じになるのですが、秘めた闘志(クールですが熱いハートを持っている)を表しています。

【その他】
株式会社ハルミナスという社名からは業務内容が推測できないので、裏面で業務内容と税理士事務所のグループ法人であることがわかるようにしたいです。

また、表面が賑やかにならない程度で「経営・財務・会計をトータル・コンサルティング」というキャッチ、又は経営・財務・会計の三項目をトライアングル(三角)に配置して下に「トータル・コンサルティング・サービス(カタカナ又は英語)」など名刺の表面で業務内容がイメージできるようだとベストです。但し、賑やかになったり、安っぽくなりそうなら省略してください。
(表面)に記載したい事項
・会社ロゴ(データがあります)
・会社名(株式会社ハルミナス)
・役職(代表取締役/人により変わります)
・名前(人により変わります)
・住所(〒610-0219 京都府京田辺市河原北町3-8-2 松浦ビル3F)
・電話番号(0774-52-8146)
・FAX番号(0774-52-8157)
・携帯電話(人により変わります)
・メールアドレス(人により変わります)
・HP(近日公開予定ですがhttp://www.hlm-bureau.jp

(裏面)に記載したい事項

【ハルミナス・グループ】

株式会社ハルミナス
【業務内容】
1.記帳・会計
2.管理会計サポート
3.財務コンサルティング
4.売上UPコンサルティング

宇野沙織税理士事務所/認定経営革新等支援機関
【業務内容】
1.税理士業務
2.節税コンサルティング
3.セカンドオピニオン

※情報の配置、デザイン等はお任せしますので、括弧や数字などは無視してください。

ロゴのイメージに合うようにお願いします
最終候補になった方に修正をお願いすることがあるかもしれませんが、当選に至らないケースもあります。但し、修正をお願いした方は参加報酬には選ばせていただきますのでご理解のほど宜しくお願いします。
表面にホームページのURLと書いていましたが、必ず表面である必要はありませんので裏面でも結構です。また、QRコードを入れて頂いても結構です。(必須ではありません)
現在、いくつか興味を持っているデザインもあるのですが、もう少し多くの提案を見たいと思いますので、締め切りを延長させていただきます。
この度は数多くのご提案ありがとうございました。
素晴らしいご提案が多数あり正直迷っています。
社内選考を行って、最終候補のご提案には修正を依頼させていただく
かもしれませんのでよろしくお願いします。

表面はシンプルなデザインですが、名刺の本来の目的である情報が見やすく、ロゴのカラーとも良く馴染んでいるのが気に入りました。
裏面のデザインは高級感、信頼感を感じるデザインでありながら、スッキリとまとまっているところが社内で高評価でした。
素晴らしい名刺をありがとうございました。

ご参加いただいた皆様、本当にありがとうございました。
素晴らしいご提案ばかりでいつもながら選択に困りましたが、良い名刺が出来て嬉しいです。

機会がございましたら別の案件でもご参加いただけたらありがたいです。

```html
<!DOCTYPE html>
<html lang="ja">
<head>
<meta charset="utf-8">
<title>株式会社ハルミナス 名刺</title>
<link href="https://fonts.googleapis.com/css2?family=Noto+Sans+JP:wght@400;500;700&family=Roboto:wght@400;500;700&display=swap" rel="stylesheet">
<style>
:root{
  --sheet:#e9e9ea;
  --label:#555;
  --blue:#1f5fae;
  --blue-dark:#174a8c;
  --band:#dfe6ee;
  --ink:#222;
  --muted:#666;
  --orange:#f0a030;
  --green:#8cbf3f;
  --circle-blue:#4d8fd0;
  --white:#fff;
}
*{margin:0;padding:0;box-sizing:border-box}
html,body{width:805px;height:1200px;overflow:hidden}
body{background:var(--sheet);font-family:"Noto Sans JP",sans-serif;color:var(--ink);position:relative}
.side-label{position:absolute;left:38px;font-family:"Roboto",sans-serif;font-size:17px;color:var(--label)}
.card{position:absolute;left:32px;width:745px;background:var(--white);box-shadow:0 2px 6px rgba(0,0,0,.18);overflow:hidden}
.card-front{top:107px;height:443px}
.card-back{top:657px;height:456px;background:var(--blue);color:var(--white)}
.edge-stripe{position:absolute;left:0;top:0;width:14px;height:100%;background:var(--blue)}
.brand{position:absolute;display:flex;align-items:center;gap:14px;font-family:"Roboto",sans-serif;font-weight:500;letter-spacing:1px}
.brand-front{left:48px;top:40px;font-size:38px;color:var(--blue-dark)}
.brand-mark{border-radius:50%;background:var(--blue)}
.brand-front .brand-mark{width:44px;height:44px}
.title{position:absolute;left:60px;top:142px;font-size:15px}
.person{position:absolute;left:60px;top:164px;display:flex;align-items:baseline;gap:16px}
.person-name{font-size:32px;font-weight:500;letter-spacing:4px}
.person-roman{font-family:"Roboto",sans-serif;font-size:15px;color:var(--muted)}
.contact{position:absolute;left:60px;display:flex;align-items:center;gap:8px;font-family:"Roboto",sans-serif;font-size:15px}
.contact svg{width:18px;height:18px}
.consult-label{position:absolute;left:600px;top:104px;font-family:"Roboto",sans-serif;font-size:14px;color:var(--muted)}
.venn{position:absolute;left:590px;top:128px}
.info-band{position:absolute;left:14px;top:290px;width:731px;height:110px;background:var(--band)}
.company{position:absolute;left:46px;top:10px;font-size:19px;font-weight:500}
.band-line{position:absolute;left:46px;display:flex;align-items:center;gap:8px;font-size:14px}
.band-line svg{width:17px;height:17px}
.url{position:absolute;left:60px;top:408px;display:flex;align-items:center;gap:8px;font-family:"Roboto",sans-serif;font-size:15px}
.url svg{width:18px;height:18px}
.group-title{position:absolute;left:40px;top:30px;display:flex;align-items:baseline;gap:18px}
.group-name{font-family:"Roboto",sans-serif;font-size:27px;font-weight:500}
.group-tagline{font-size:14px}
.group-rule{position:absolute;left:40px;top:76px;width:690px;height:1px;background:rgba(255,255,255,.7)}
.services{position:absolute;list-style:none;font-size:15px}
.services li{height:37px;display:flex;align-items:center;gap:10px}
.services .head{font-weight:500}
.services .bullet{width:9px;height:9px;background:var(--white)}
.services-left{left:56px;top:114px}
.office{position:absolute;left:370px;top:112px}
.office-name{font-size:16px;font-weight:500}
.office-note{font-size:13px;margin-top:8px}
.services-right{left:370px;top:208px}
.brand-back{right:36px;top:340px;flex-direction:column;gap:10px;font-size:22px;color:var(--white)}
.brand-back .brand-mark{width:58px;height:58px;background:var(--white)}
</style>
</head>
<body>
<div class="side-label" style="top:74px">Front</div>
<section class="card card-front">
  <div class="edge-stripe"></div>
  <div class="brand brand-front"><span class="brand-mark"></span>HALMINAS</div>

  <div class="title">代表取締役</div>
  <div class="person"><span class="person-name">川村 健一</span><span class="person-roman">Kenichi Kawamura</span></div>
  <div class="contact" style="top:206px">
    <svg viewBox="0 0 18 18"><rect x="4" y="1" width="10" height="16" rx="2" fill="var(--blue)"/><rect x="6" y="3" width="6" height="10" fill="#fff"/></svg>090-1234-5678</div>
  <div class="contact" style="top:236px">
    <svg viewBox="0 0 18 18"><rect x="1" y="4" width="16" height="11" rx="1" fill="var(--blue)"/><path d="M2 5l7 6 7-6" stroke="#fff" stroke-width="1.4" fill="none"/></svg>info@example.com</div>

  <div class="consult-label">Total Consulting</div>
  <svg class="venn" width="140" height="130" viewBox="0 0 140 130" font-family="Noto Sans JP, sans-serif" font-size="12" fill="none" stroke-width="3">
    <circle cx="70" cy="40" r="34" stroke="var(--orange)"/>
    <circle cx="45" cy="85" r="34" stroke="var(--circle-blue)"/>
    <circle cx="95" cy="85" r="34" stroke="var(--green)"/>
    <text x="70" y="30" text-anchor="middle" fill="var(--ink)" stroke="none">経営</text>
    <text x="38" y="100" text-anchor="middle" fill="var(--ink)" stroke="none">財務</text>
    <text x="102" y="100" text-anchor="middle" fill="var(--ink)" stroke="none">会計</text>
  </svg>

  <div class="info-band">
    <div class="company">株式会社ハルミナス</div>
    <div class="band-line" style="top:44px">
      <svg viewBox="0 0 18 18"><path d="M2 9l7-7 7 7v8H2z" fill="var(--blue)"/></svg>〒610-0219 京都府京田辺市河原北町3-8-2 松浦ビル3F</div>
    <div class="band-line" style="top:74px">
      <svg viewBox="0 0 18 18"><path d="M4 2h3l1 4-2 1a9 9 0 0 0 5 5l1-2 4 1v3a2 2 0 0 1-2 2C7 16 2 11 2 4a2 2 0 0 1 2-2z" fill="var(--blue)"/></svg>0774-52-8146
      <span style="width:20px"></span>
      <svg viewBox="0 0 18 18"><rect x="1" y="6" width="16" height="10" rx="1" fill="var(--blue)"/><rect x="5" y="2" width="8" height="6" fill="var(--blue)"/><rect x="4" y="9" width="10" height="2" fill="#fff"/></svg>0774-52-8157</div>
  </div>

  <div class="url">
    <svg viewBox="0 0 18 18"><circle cx="9" cy="9" r="7" fill="none" stroke="var(--blue)" stroke-width="1.6"/><path d="M2 9h14M9 2c-4 4-4 10 0 14M9 2c4 4 4 10 0 14" stroke="var(--blue)" stroke-width="1.2" fill="none"/></svg>http://www.hlm-bureau.jp</div>
</section>

<div class="side-label" style="top:622px">Back</div>
<section class="card card-back">
  <div class="group-title"><span class="group-name">Halminas Group</span><span class="group-tagline">経営・財務・会計をトータル・コンサルティング</span></div>
  <div class="group-rule"></div>

  <ul class="services services-left">
    <li class="head">【業務内容】</li>
    <li><span class="bullet"></span>記帳・会計</li>
    <li><span class="bullet"></span>管理会計サポート</li>
    <li><span class="bullet"></span>財務コンサルティング</li>
    <li><span class="bullet"></span>売上UPコンサルティング</li>
  </ul>

  <div class="office">
    <div class="office-name">宇野沙織税理士事務所</div>
    <div class="office-note">認定経営革新等支援機関</div>
  </div>
  <ul class="services services-right">
    <li class="head">【業務内容】</li>
    <li><span class="bullet"></span>税理士業務</li>
    <li><span class="bullet"></span>節税コンサルティング</li>
    <li><span class="bullet"></span>セカンドオピニオン</li>
  </ul>

  <div class="brand brand-back"><span class="brand-mark"></span>HALMINAS</div>
</section>
</body>
</html>
```